The Brightway Surgery Stationary (Medical)

Stationery for The Brightway surgery
using existing logos
Please also add a green apple if possible on another corner away from the logo on some of your designs

Please take a look at www.thebrightwaysurgery.com.au so you can get a feel for what The Brightway Surgery offers our clients.

Stationary Required: business cards, letter head, comp slips

I do not require envelopes or invoives.

Target Market(s)

The general popultation needing medical care
Professionals
Mums & Dads
Elderly

Industry/Entity Type

Business

Requirements
Must have
• Company Logo

Address
Email
Website
Phone
Should not have
• Traditional Medical Icons
No Times New Roman

```html
<!DOCTYPE html>
<html lang="en">
<head>
<meta charset="utf-8">
<title>The Brightway Surgery – Letterhead</title>
<link rel="stylesheet" href="https://fonts.googleapis.com/css2?family=Arimo:wght@400&display=swap">
<style>
  :root {
    --canvas: #f4f4f4;
    --sheet: #ffffff;
    --sheet-edge: #e2e2e2;
    --ink: #3a3a3a;
    --ink-soft: #555555;
    --brand-blue: #29aad6;
    --apple-light: #a8d84a;
    --apple-dark: #4e9a1c;
    --signature-tone: #f1f1f1;
    --bar-top: #4a4a4a;
    --bar-bottom: #0e0e0e;
  }
  html, body {
    margin: 0;
    padding: 0;
    width: 947px;
    height: 1200px;
    overflow: hidden;
    background: var(--canvas);
  }
  .letterhead {
    position: relative;
    width: 947px;
    height: 1200px;
    font-family: "Arimo", Arial, sans-serif;
    color: var(--ink);
  }
  .sheet {
    position: absolute;
    left: 30px;
    top: 47px;
    width: 872px;
    height: 1121px;
    background: var(--sheet);
    border: 1px solid var(--sheet-edge);
    box-shadow: 4px 3px 4px rgba(0,0,0,0.08);
  }
  .brand {
    position: absolute;
    left: 60px;
    top: 118px;
    display: flex;
    align-items: center;
    gap: 10px;
  }
  .brand-dot {
    width: 34px;
    height: 34px;
    border-radius: 50%;
    background: var(--brand-blue);
  }
  .brand-name {
    font-size: 18px;
    line-height: 20px;
    width: 120px;
    color: var(--brand-blue);
  }
  .date {
    position: absolute;
    right: 239px;
    top: 205px;
    font-size: 13.8px;
    line-height: 17px;
  }
  .body-copy {
    position: absolute;
    left: 230px;
    top: 238px;
    width: 478px;
    font-size: 13.8px;
    line-height: 17px;
    text-align: justify;
  }
  .body-copy p { margin: 0 0 18px; }
  .body-copy p.section-break { margin-top: 33px; }
  .signature {
    position: absolute;
    left: 545px;
    top: 890px;
    width: 195px;
    height: 75px;
    background: linear-gradient(90deg, var(--signature-tone), #fbfbfb);
  }
  .contact {
    position: absolute;
    right: 144px;
    top: 1047px;
    text-align: right;
    font-size: 11px;
    line-height: 14.5px;
    color: var(--ink-soft);
  }
  .apple {
    position: absolute;
    left: 818px;
    top: 1047px;
    width: 56px;
    height: 66px;
    border-radius: 45% 45% 48% 48%;
    background: radial-gradient(circle at 38% 40%, var(--apple-light), var(--apple-dark));
  }
  .footer-bar {
    position: absolute;
    left: 48px;
    top: 1137px;
    width: 837px;
    height: 17px;
    background: linear-gradient(var(--bar-top), var(--bar-bottom));
  }
</style>
</head>
<body>
<main class="letterhead">
  <div class="sheet"></div>

  <header class="brand">
    <span class="brand-dot"></span>
    <span class="brand-name">The Brightway Surgery</span>
  </header>

  <div class="date">10th Jan 2011</div>

  <section class="body-copy">
    <p>Lorem Ipsum is simply dummy text of the printing and typesetting industry. Lorem Ipsum has been the industry's standard dummy text ever since the 1500s, when an unknown printer took a galley of type and scrambled it to make a type specimen book. It has survived not only five centuries, but also the leap into electronic typesetting, remaining essentially unchanged. It was popularised in the 1960s with the release of Typeset sheets containing Lorem Ipsum passages, and more recently with desktop publishing software like Pagecraft Studio including versions of Lorem Ipsum.</p>
    <p>It is a long established fact that a reader will be distracted by the readable content of a page when looking at its layout. The point of using Lorem Ipsum is that it has a more-or-less normal distribution of letters, as opposed to using 'Content here, content here', making it look like readable English. Many desktop publishing packages and web page editors now use Lorem Ipsum as their default model text, and a search for 'lorem ipsum' will uncover many web sites still in their infancy. Various versions have evolved over the years, sometimes by accident, sometimes on purpose (injected humour and the like).</p>
    <p class="section-break">Contrary to popular belief, Lorem Ipsum is not simply random text. It has roots in a piece of classical Latin literature from 45 BC, making it over 2000 years old. Richard Ashworth, a Latin professor at Hollis-Grange College in Virginia, looked up one of the more obscure Latin words, consec&shy;tetur, from a Lorem Ipsum passage, and going through the cites of the word in classical literature, discovered the undoubtable source. Lorem Ipsum comes from sections 1.10.32 and 1.10.33 of "de Ordine Virtutum et Vitio&shy;rum" (The Order of Virtue and Vice) by Varennus, written in 45 BC. This book is a treatise on the theory of ethics, very popular during the Renaissance. The first line of Lorem Ipsum, "Lorem ipsum dolor sit amet..", comes from a line in section 1.10.32.</p>
    <p>The standard chunk of Lorem Ipsum used since the 1500s is reproduced below for those interested. Sections 1.10.32 and 1.10.33 from "de Ordine Virtutum et Vitiorum" by Varennus are also reproduced in their exact original form, accompanied by English versions from the 1914 translation by H. Merriden.</p>
  </section>

  <div class="signature" role="img" aria-label="Handwritten signature"></div>

  <footer class="contact">
    The Brightway Surgery (Inside Cornerstone Pharmacy) | Shop 4, Larkfield<br>
    Market Place |&nbsp; 8 - 16 The Ridgeway Larkfield 2154<br>
    Te: 02.9000.4812<br>
    Email: larkfield@thebrightwaysurgery.com.au<br>
    www.thebrightwaysurgery.com.au
  </footer>

  <div class="apple" role="img" aria-label="Photograph of a green apple"></div>

  <div class="footer-bar"></div>
</main>
</body>
</html>
```